Fabric Softener

We need fabric softener. Bottle picture attached for reference. Color of bottle can be proposed as well. Normally bottle is pink and blue color

Logo is also attached that shall be used.
Updates

Need extra days to review

Low designer entries

Target Market(s)

Niche

Font styles to use
Sans Serif

Requirements
Must have
• Fabric, Brightness, Nature
Nice to have
• Good colors
Should not have
• Adults

```html
<!DOCTYPE html>
<html lang="en">
<head>
<meta charset="utf-8">
<title>Softara Fabric Softener Label</title>
<link rel="stylesheet" href="https://fonts.googleapis.com/css2?family=Open+Sans:wght@700;800&family=Oswald:wght@500;600&display=swap">
<style>
  :root {
    --page: #ffffff;
    --label-purple: #5a0f66;
    --label-deep: #3a0846;
    --magenta: #c4155f;
    --violet: #8a1a8f;
    --banner: #6b3fa8;
    --ribbon: #4a3aa0;
    --white: #ffffff;
    --soft-white: #f3e6f5;
  }
  * { box-sizing: border-box; margin: 0; padding: 0; }
  html, body { width: 1200px; height: 900px; overflow: hidden; background: var(--page); }
  .canvas { position: relative; width: 1200px; height: 900px; background: var(--page); }

  .label {
    position: absolute; left: 330px; top: 60px; width: 540px; height: 780px;
    border-radius: 28px; overflow: hidden;
    background: linear-gradient(180deg, var(--label-purple) 0%, var(--label-deep) 55%, var(--violet) 100%);
  }
  .glow-art {
    position: absolute; left: 0; top: 0; width: 100%; height: 380px;
    background: radial-gradient(ellipse at 40% 25%, #f7c9de 0%, var(--magenta) 28%, #7a1470 62%, var(--label-purple) 100%);
  }
  .fabric-art {
    position: absolute; left: 0; top: 400px; width: 100%; height: 220px;
    background: linear-gradient(170deg, var(--label-deep) 0%, #7b1580 45%, #b0247f 60%, #4a0a55 100%);
  }

  .ribbon {
    position: absolute; left: 30px; top: 120px; padding: 8px 26px 8px 22px;
    background: var(--ribbon); color: var(--white);
    font: 800 20px/1 "Open Sans", sans-serif; letter-spacing: 2px;
    transform: rotate(-6deg);
  }
  .brand-band {
    position: absolute; left: 40px; top: 170px; width: 400px; height: 150px;
    background: var(--banner); border-radius: 18px;
    display: flex; align-items: center; justify-content: center;
  }
  .brand-name {
    font: 800 72px/1 "Open Sans", sans-serif; color: var(--white);
  }

  .product-type {
    position: absolute; left: 40px; top: 352px;
    font: 700 26px/1 "Open Sans", sans-serif; color: var(--white); letter-spacing: 0.5px;
  }
  .loads-badge {
    position: absolute; left: 410px; top: 330px; width: 72px; height: 72px; border-radius: 50%;
    background: var(--white); color: var(--label-purple);
    display: flex; flex-direction: column; align-items: center; justify-content: center;
  }
  .loads-badge .count { font: 800 28px/1 "Open Sans", sans-serif; }
  .loads-badge .unit { font: 700 10px/1.2 "Open Sans", sans-serif; letter-spacing: 1px; }

  .warnings {
    position: absolute; left: 30px; top: 640px; width: 480px;
    font: 500 13px/1.3 "Oswald", sans-serif; color: var(--soft-white);
  }
  .warnings strong { font-weight: 600; color: var(--white); }
  .volume {
    position: absolute; left: 0; top: 690px; width: 100%; text-align: center;
    font: 600 22px/1.25 "Oswald", sans-serif; color: var(--white);
  }
</style>
</head>
<body>
  <main class="canvas">
    <section class="label">
      <div class="glow-art" role="img" aria-label="Soft magenta glow with floating bokeh bubbles"></div>
      <div class="fabric-art" role="img" aria-label="Flowing purple satin fabric with bubbles"></div>

      <div class="ribbon">ORIGINAL</div>
      <div class="brand-band">
        <span class="brand-name">Softara</span>
      </div>

      <h1 class="product-type">FABRIC SOFTENER</h1>
      <div class="loads-badge">
        <span class="count">60</span>
        <span class="unit">LOADS</span>
      </div>

      <p class="warnings">
        <strong>CAUTION:</strong> EYE IRRITANT. HARMFUL IF SWALLOWED. SEE BACK LABEL<br>
        <strong>ATTENTION:</strong> IRRITE LES YEUX. NOCIF SI INGÉRÉ. LIRE L'ÉTIQUETTE AU DOS.
      </p>
      <p class="volume">2.72 L (2.87 US QT/PTE É.-U.)<br>92 FL OZ LIQ.</p>
    </section>
  </main>
</body>
</html>
```